Morvela Aesthetic Doctor

I require an elegant, luxurious looking business card for my aesthetic business. I am a doctor and that will set me aside from competitors. I am planning to provide home and spa based treatments to clients with high expectations. I have attached my logo.

```html
<!DOCTYPE html>
<html lang="en">
<head>
<meta charset="utf-8">
<title>Morvela Aesthetic Doctor – Business Card</title>
<link href="https://fonts.googleapis.com/css2?family=Lato:wght@400;700&display=swap" rel="stylesheet">
<style>
  :root {
    --page: #ececec;
    --card: #ffffff;
    --aqua: #7ffdf5;
    --sky: #5ccdf2;
    --slate: #8c9fa4;
    --ink: #555b5e;
    --on-aqua: #ffffff;
  }
  * { box-sizing: border-box; margin: 0; padding: 0; }
  html, body { width: 1000px; height: 1200px; overflow: hidden; }
  body {
    background: var(--page);
    font-family: "Lato", sans-serif;
    position: relative;
  }
  .card {
    position: absolute;
    left: 126px;
    width: 748px;
    height: 450px;
    background: var(--card);
    overflow: hidden;
  }
  .card--front { top: 106px; }
  .card--back { top: 637px; }

  /* Wordmark */
  .wordmark {
    position: absolute;
    display: flex;
    align-items: center;
    gap: 12px;
    color: var(--slate);
    font-weight: 400;
  }
  .wordmark__dot {
    width: 44px; height: 44px;
    border: 2px solid var(--slate);
    border-radius: 50%;
    flex: none;
  }
  .wordmark__name { line-height: 1.05; letter-spacing: 0.04em; }

  /* Front */
  .front__rule {
    position: absolute;
    top: 181px;
    height: 3px;
    background: var(--sky);
  }
  .front__rule--left { left: 0; width: 240px; }
  .front__rule--right { right: 0; width: 240px; }
  .card--front .wordmark {
    left: 254px; top: 157px; width: 240px;
    font-size: 19px;
  }
  .band {
    position: absolute;
    left: 0; right: 0;
    background: var(--aqua);
    color: var(--on-aqua);
    text-align: center;
  }
  .front__band { top: 352px; bottom: 0; }
  .front__tagline { margin-top: 29px; font-size: 15px; }

  /* Back */
  .back__identity .wordmark {
    left: 115px; top: 88px; width: 200px;
    font-size: 15px; gap: 10px;
  }
  .back__identity .wordmark__dot { width: 36px; height: 36px; }
  .back__rule {
    position: absolute;
    left: 91px; top: 178px;
    width: 240px; height: 3px;
    background: var(--sky);
  }
  .back__name {
    position: absolute;
    left: 91px; top: 204px; width: 240px;
    text-align: center;
    font-size: 15px;
    color: var(--ink);
  }
  .back__credentials {
    position: absolute;
    left: 71px; top: 245px; width: 280px;
    text-align: center;
    font-size: 10.5px;
    line-height: 19px;
    color: var(--sky);
  }
  .back__panel {
    position: absolute;
    left: 400px; top: 0;
    width: 348px; height: 335px;
    background: var(--aqua);
  }
  .contact {
    position: absolute;
    left: 376px;
    display: flex;
    align-items: center;
    height: 48px;
  }
  .contact__icon {
    width: 48px; height: 48px;
    display: flex; align-items: center; justify-content: center;
  }
  .contact__bump {
    position: absolute;
    left: 0; top: 0;
    width: 48px; height: 48px;
    border-radius: 50%;
    background: var(--card);
    clip-path: inset(0 0 0 24px);
  }
  .contact__icon svg { position: relative; }
  .contact__text {
    position: absolute;
    left: 73px;
    white-space: nowrap;
    font-size: 17px;
    color: var(--on-aqua);
  }
  .contact--phone { top: 73px; }
  .contact--mail { top: 156px; }
  .contact--web { top: 238px; }

  .back__band { top: 340px; bottom: 0; }
  .back__services {
    margin-top: 18px;
    font-size: 12.5px;
    line-height: 16.5px;
  }
</style>
</head>
<body>

<section class="card card--front">
  <div class="front__rule front__rule--left"></div>
  <div class="wordmark">
    <span class="wordmark__dot"></span>
    <span class="wordmark__name">Morvela<br>Aesthetic Doctor</span>
  </div>
  <div class="front__rule front__rule--right"></div>
  <div class="band front__band">
    <p class="front__tagline">Home and Spa Based Treatments</p>
  </div>
</section>

<section class="card card--back">
  <div class="back__identity">
    <div class="wordmark">
      <span class="wordmark__dot"></span>
      <span class="wordmark__name">Morvela<br>Aesthetic Doctor</span>
    </div>
    <div class="back__rule"></div>
    <p class="back__name">Dr Elin Varga</p>
    <p class="back__credentials">MRCPCH MD Australasian Diploma<br>of Aesthetic Medicine</p>
  </div>

  <div class="back__panel"></div>

  <div class="contact contact--phone">
    <div class="contact__icon">
      <span class="contact__bump"></span>
      <svg width="22" height="22" viewBox="0 0 24 24" aria-hidden="true">
        <path fill="#5ccdf2" d="M6.6 10.8a15.1 15.1 0 0 0 6.6 6.6l2.2-2.2c.3-.3.7-.4 1-.2 1.1.4 2.3.6 3.6.6.6 0 1 .4 1 1V20c0 .6-.4 1-1 1A17 17 0 0 1 3 4c0-.6.4-1 1-1h3.5c.6 0 1 .4 1 1 0 1.3.2 2.5.6 3.6.1.3 0 .7-.2 1z"/>
      </svg>
    </div>
    <span class="contact__text">0800 555 014</span>
  </div>

  <div class="contact contact--mail">
    <div class="contact__icon">
      <span class="contact__bump"></span>
      <svg width="28" height="20" viewBox="0 0 28 20" aria-hidden="true">
        <rect width="28" height="20" rx="2" fill="#5ccdf2"/>
        <path d="M2 3l12 9 12-9M2 18l9-7M26 18l-9-7" fill="none" stroke="#fff" stroke-width="1.2"/>
      </svg>
    </div>
    <span class="contact__text">elin@morvela.co.nz</span>
  </div>

  <div class="contact contact--web">
    <div class="contact__icon">
      <span class="contact__bump"></span>
      <svg width="30" height="30" viewBox="0 0 30 30" aria-hidden="true">
        <g fill="none" stroke="#5ccdf2" stroke-width="1.4">
          <circle cx="15" cy="15" r="13"/>
          <ellipse cx="15" cy="15" rx="6" ry="13"/>
          <path d="M15 2v26M2 15h26M4 8h22M4 22h22"/>
        </g>
      </svg>
    </div>
    <span class="contact__text">www.morvela.co.nz</span>
  </div>

  <div class="band back__band">
    <p class="back__services">
      Dermal injectables - Plasma facials - Microneedling<br>
      Skin boosters - Excessive sweating<br>
      Home and Spa Based Treatments
    </p>
  </div>
</section>

</body>
</html>
```